Varnel Disaster Response Team Van Wrap

Designing a wrap for our Disaster Response Team vans. We do flood, fire and mold insurance claim work. Looking for possible black fully wrapped van with large logo on the sides and on back of van. We will have to have the QADTM number and the LRW numbers in smaller letters along the bottom of sides and on back of van.
Updates

Wanting to give some extra time to designers to make some changes

Need extra days to review

Target Market(s)

Commerical and Residential Owners

Industry/Entity Type

Insurance restoration

Requirements
Must have
• 1-888-4VARNEL / www.varnelinc.example / FIRE / FLOOD / MOLD / ROOFING / QADTM # 52906431 / OK LRW # 61548820, Commercial Endorsement
Nice to have
• Want a full color wrap on a 2024 Halcor Brisk Voyanter 3500 EXT van. Maybe have a black background. The logo is black so may need to do some outlining for that. Also open to using one of the colors in the logo for the background. We do fire, flood, mold remediation and roofing. We will want the phone number and website to be in various places on sides and back.

```html
<!DOCTYPE html>
<html lang="en">
<head>
<meta charset="utf-8">
<title>Varnel Disaster Response Team – Van Wrap Side Panels</title>
<link rel="stylesheet" href="https://fonts.googleapis.com/css2?family=Oswald:wght@500&family=Poppins:wght@500;600;700&family=Cinzel:wght@500&display=swap">
<style>
  :root {
    --wrap-black: #0b0b0c;
    --wrap-orange: #f29a1c;
    --wrap-orange-deep: #e27d0e;
    --wrap-gold: #c7972f;
    --accent-orange: #f3951f;
    --accent-blue: #2d8fd3;
    --accent-red: #d3334f;
    --accent-green: #6bb43f;
    --badge-silver: #e7e8ea;
    --text-white: #ffffff;
    --page-bg: #ffffff;
  }
  html, body {
    margin: 0;
    width: 1200px;
    height: 1200px;
    overflow: hidden;
    background: var(--page-bg);
  }
  .canvas {
    position: relative;
    width: 1200px;
    height: 1200px;
  }
  .wrap-panel {
    position: absolute;
    left: 60px;
    width: 1080px;
    height: 420px;
    border-radius: 28px;
    overflow: hidden;
  }
  .wrap-panel--gold { top: 130px; }
  .wrap-panel--silver { top: 650px; }
  .panel-art {
    position: absolute;
    inset: 0;
  }
  .endorsement {
    position: absolute;
    left: 40px;
    top: 46px;
    margin: 0;
    font-family: "Oswald", sans-serif;
    font-weight: 500;
    font-size: 22px;
    letter-spacing: 1.5px;
    color: var(--accent-orange);
  }
  .phone {
    position: absolute;
    left: 40px;
    top: 104px;
    margin: 0;
    font-family: "Poppins", sans-serif;
    font-weight: 700;
    font-size: 28px;
    color: var(--text-white);
  }
  .website {
    position: absolute;
    left: 40px;
    top: 146px;
    margin: 0;
    font-family: "Poppins", sans-serif;
    font-weight: 500;
    font-size: 19px;
    letter-spacing: 1px;
    color: var(--accent-blue);
  }
  .services {
    position: absolute;
    left: 40px;
    top: 232px;
    margin: 0;
    padding: 0;
    list-style: none;
    display: flex;
    align-items: center;
    gap: 6px;
    font-family: "Oswald", sans-serif;
    font-weight: 500;
    font-size: 22px;
    color: var(--text-white);
  }
  .services .dot {
    width: 8px; height: 8px; border-radius: 50%;
    display: inline-block;
  }
  .dot--fire { background: var(--accent-orange); }
  .dot--flood { background: var(--accent-blue); }
  .dot--mold { background: var(--accent-blue); }
  .dot--roof { background: var(--accent-green); }
  .brand-block {
    position: absolute;
    left: 330px;
    top: 118px;
    width: 360px;
    text-align: center;
  }
  .brand-name {
    display: flex;
    align-items: center;
    justify-content: center;
    gap: 16px;
    margin: 0;
    font-family: "Poppins", sans-serif;
    font-weight: 600;
    font-size: 64px;
    line-height: 1;
    letter-spacing: 3px;
    color: var(--text-white);
  }
  .brand-mark {
    width: 26px; height: 26px;
    display: inline-block;
  }
  .wrap-panel--gold .brand-mark { background: var(--wrap-gold); }
  .wrap-panel--silver .brand-mark { background: var(--badge-silver); }
  .brand-tagline {
    margin: 16px 0 0;
    font-family: "Cinzel", serif;
    font-weight: 500;
    font-size: 20px;
    letter-spacing: 1px;
    color: var(--text-white);
  }
  .cert-block {
    position: absolute;
    left: 930px;
    top: 190px;
    width: 130px;
  }
  .cert-badge {
    width: 46px;
    height: 58px;
    border-radius: 4px;
    background: var(--badge-silver);
    margin-bottom: 10px;
  }
  .cert-numbers {
    margin: 0;
    font-family: "Poppins", sans-serif;
    font-weight: 600;
    font-size: 11px;
    line-height: 1.35;
    color: var(--wrap-black);
  }
</style>
</head>
<body>
<main class="canvas">

  <section class="wrap-panel wrap-panel--gold" aria-label="Van wrap side, gold trim version">
    <svg class="panel-art" viewBox="0 0 1080 420" preserveAspectRatio="none">
      <defs>
        <linearGradient id="orange-side-a" x1="0" y1="0" x2="0" y2="1">
          <stop offset="0" stop-color="#f4a625"/>
          <stop offset="1" stop-color="#e27d0e"/>
        </linearGradient>
      </defs>
      <rect width="1080" height="420" fill="var(--wrap-black)"/>
      <path d="M520 0 H1080 V420 H700 C640 300 600 120 520 0 Z" fill="url(#orange-side-a)"/>
      <rect x="0" y="370" width="1080" height="50" fill="var(--wrap-black)"/>
      <path d="M250 372 H1080 V384 H250 Z" fill="var(--wrap-gold)"/>
    </svg>
    <p class="endorsement">COMMERCIAL ENDORSEMENT</p>
    <p class="phone">1-888-4VARNEL</p>
    <p class="website">www.varnelinc.example</p>
    <ul class="services">
      <li>FIRE</li><li><span class="dot dot--fire"></span></li>
      <li>FLOOD</li><li><span class="dot dot--flood"></span></li>
      <li>MOLD</li><li><span class="dot dot--roof"></span></li>
      <li>ROOFING</li>
    </ul>
    <div class="brand-block">
      <h1 class="brand-name"><span class="brand-mark"></span>VARNEL</h1>
      <p class="brand-tagline">DISASTER RESPONSE TEAM</p>
    </div>
    <div class="cert-block">
      <div class="cert-badge"></div>
      <p class="cert-numbers">QADTM # 52906431<br>OK LRW # 61548820</p>
    </div>
  </section>

  <section class="wrap-panel wrap-panel--silver" aria-label="Van wrap side, silver trim version">
    <svg class="panel-art" viewBox="0 0 1080 420" preserveAspectRatio="none">
      <defs>
        <linearGradient id="orange-side-b" x1="0" y1="0" x2="0" y2="1">
          <stop offset="0" stop-color="#f4a625"/>
          <stop offset="1" stop-color="#e27d0e"/>
        </linearGradient>
      </defs>
      <rect width="1080" height="420" fill="var(--wrap-black)"/>
      <path d="M520 0 H1080 V420 H700 C640 300 600 120 520 0 Z" fill="url(#orange-side-b)"/>
      <rect x="0" y="370" width="1080" height="50" fill="var(--wrap-black)"/>
      <path d="M250 372 H1080 V384 H250 Z" fill="var(--wrap-gold)"/>
    </svg>
    <p class="endorsement">COMMERCIAL ENDORSEMENT</p>
    <p class="phone">1-888-4VARNEL</p>
    <p class="website">www.varnelinc.example</p>
    <ul class="services">
      <li>FIRE</li><li><span class="dot dot--fire"></span></li>
      <li>FLOOD</li><li><span class="dot dot--flood"></span></li>
      <li>MOLD</li><li><span class="dot dot--roof"></span></li>
      <li>ROOFING</li>
    </ul>
    <div class="brand-block">
      <h2 class="brand-name"><span class="brand-mark"></span>VARNEL</h2>
      <p class="brand-tagline">DISASTER RESPONSE TEAM</p>
    </div>
    <div class="cert-block">
      <div class="cert-badge"></div>
      <p class="cert-numbers">QADTM # 52906431<br>OK LRW # 61548820</p>
    </div>
  </section>

</main>
</body>
</html>
```